Executive & Leadership Coach needs a Graphic Design

We need a graphic design for a Leadership methodology/strategy that can be linked to The Harbor Prism

The Harbor Prism consists of:
1. Achievements
2. Personal Brand
3. Network
4. Executive Presence

This should Graphic Design will need to be used in PowerPoint presentations, training manuals and web pages

The design should be modern and provide the feeling of strength, trust, energy & creativity

Industry/Entity Type

Graphic Design

Other font styles liked:
• Calibri, Verdana

```html
<!DOCTYPE html>
<html lang="en">
<head>
<meta charset="utf-8">
<title>The Harbor Prism</title>
<link href="https://fonts.googleapis.com/css2?family=Open+Sans:wght@400;700&display=swap" rel="stylesheet">
<style>
  :root {
    --bg: #ffffff;
    --ring-red: #c4262e;
    --blue: #0070bb;
    --green: #3db54a;
    --purple: #652d90;
    --magenta: #ff00ff;
    --hub-fill: #e4e4e4;
    --hub-edge: #bdbdbd;
    --hub-text: #1e1e1e;
    --label: #ffffff;
  }
  html, body {
    margin: 0;
    padding: 0;
    width: 1200px;
    height: 900px;
    overflow: hidden;
    background: var(--bg);
  }
  .canvas {
    width: 1200px;
    height: 900px;
    display: block;
  }
  .prism-wheel { display: block; }
  .ring-band { fill: none; stroke: var(--ring-red); stroke-width: 11; }
  .ring-line { fill: none; stroke: #ffffff; stroke-width: 2; }
  .ring-arrow { fill: #ffffff; }
  .segment { stroke: #ffffff; stroke-width: 4; stroke-linejoin: round; }
  .segment--presence { fill: var(--blue); }
  .segment--achievements { fill: var(--green); }
  .segment--network { fill: var(--purple); }
  .segment--personal { fill: var(--magenta); }
  .segment-label {
    font-family: "Open Sans", Calibri, sans-serif;
    font-size: 30px;
    font-weight: 400;
    fill: var(--label);
  }
  .hub-shadow { fill: #000; opacity: 0.18; }
  .hub { fill: var(--hub-fill); stroke: url(#hubEdge); stroke-width: 9; }
  .hub-title {
    font-family: "Open Sans", Calibri, sans-serif;
    font-size: 44px;
    font-weight: 700;
    fill: var(--hub-text);
    text-anchor: middle;
  }
</style>
</head>
<body>
<main class="canvas">
  <svg class="prism-wheel" width="1200" height="900" viewBox="0 0 1024 768" aria-label="The Harbor Prism: Executive Presence, Achievements, Network, Personal">
    <defs>
      <linearGradient id="hubEdge" x1="0" y1="0" x2="0" y2="1">
        <stop offset="0" stop-color="#f4f4f4"/>
        <stop offset="1" stop-color="#a9a9a9"/>
      </linearGradient>
      <filter id="hubBlur" x="-30%" y="-30%" width="160%" height="160%">
        <feGaussianBlur stdDeviation="6"/>
      </filter>
      <path id="arcPresence" d="M275 320 A245 245 0 0 1 512 138"/>
      <path id="arcAchievements" d="M589 171 A225 225 0 0 1 730 329"/>
    </defs>

    <!-- outer ring -->
    <circle class="ring-band" cx="512" cy="383" r="289"/>
    <circle class="ring-line" cx="512" cy="383" r="289"/>

    <!-- wheel segments -->
    <path class="segment segment--presence"
      d="M230 365 A282 282 0 0 1 505 101 C600 170 640 260 636 350 A128 128 0 0 0 478 262 C380 255 280 300 230 365 Z"/>
    <path class="segment segment--achievements"
      d="M505 101 A282 282 0 0 1 794 385 C720 470 630 510 545 504 A128 128 0 0 0 636 350 C640 260 600 170 505 101 Z"/>
    <path class="segment segment--network"
      d="M794 385 A282 282 0 0 1 512 665 C420 590 385 500 388 415 A128 128 0 0 0 545 504 C630 510 720 470 794 385 Z"/>
    <path class="segment segment--personal"
      d="M512 665 A282 282 0 0 1 230 365 C280 300 380 255 478 262 A128 128 0 0 0 388 415 C385 500 420 590 512 665 Z"/>

    <!-- ring direction markers -->
    <path class="ring-arrow" d="M488 94 l10 5 -10 5 z M498 94 l10 5 -10 5 z"/>
    <path class="ring-arrow" d="M796 360 l5 10 5 -10 z M796 370 l5 10 5 -10 z"/>
    <path class="ring-arrow" d="M525 667 l-10 5 10 5 z M515 667 l-10 5 10 5 z"/>
    <path class="ring-arrow" d="M218 395 l5 -10 5 10 z M218 405 l5 -10 5 10 z"/>

    <!-- labels -->
    <text class="segment-label"><textPath href="#arcPresence" startOffset="50%" text-anchor="middle">Executive Presence</textPath></text>
    <text class="segment-label"><textPath href="#arcAchievements" startOffset="50%" text-anchor="middle">Achievements</textPath></text>
    <text class="segment-label" text-anchor="middle" transform="translate(658 578) rotate(-32)">Network</text>
    <text class="segment-label" text-anchor="middle" transform="translate(318 524) rotate(58)">Personal</text>

    <!-- hub -->
    <circle class="hub-shadow" cx="514" cy="388" r="124" filter="url(#hubBlur)"/>
    <circle class="hub" cx="512" cy="383" r="120"/>
    <text class="hub-title" x="512" y="370">Harbor</text>
    <text class="hub-title" x="512" y="422">Prism</text>
  </svg>
</main>
</body>
</html>
```